Pebble

My company name is pebble. The logo is attached. I am the business owner.
Name Gideon Thorpe
Phone number- 5553018826
email- Gideon_thorpe@quillnet.net
Website is not live yet but it will be workwithpebble.com
the current beta link is- https://site.brvhosting.com/pebble-v3/
on the back write “ find creative pros”
Use that beta link as reference for typography and colors on card.

```html
<!DOCTYPE html>
<html lang="en">
<head>
<meta charset="UTF-8">
<title>Pebble — Business Card</title>
<link rel="stylesheet" href="https://fonts.googleapis.com/css2?family=Montserrat:wght@400;600;800&display=swap">
<style>
  :root {
    --canvas: #e9e9e9;
    --card-dark: #262626;
    --card-light: #f4f4f4;
    --mark-grey: #c9c9c9;
    --mark-faint: #bdbdbd;
    --ink: #2a2a2a;
    --ink-soft: #3a3a3a;
    --note-light: #9a9a9a;
    --accent: #e5801d;
    --white: #ffffff;
  }
  * { box-sizing: border-box; margin: 0; padding: 0; }
  html, body { width: 1200px; height: 900px; overflow: hidden; }
  body {
    background: var(--canvas);
    font-family: "Montserrat", sans-serif;
    display: flex;
    align-items: center;
    justify-content: center;
    gap: 40px;
  }
  .card {
    width: 520px;
    height: 297px;
    position: relative;
    overflow: hidden;
    box-shadow: 0 10px 30px rgba(0,0,0,0.18);
  }

  .wordmark {
    font-weight: 800;
    letter-spacing: -1px;
    text-transform: uppercase;
    line-height: 1;
    white-space: nowrap;
  }

  /* Back */
  .card--back {
    background: var(--card-dark);
  }
  .card--back .wordmark {
    position: absolute;
    left: 0;
    right: 0;
    top: 108px;
    text-align: center;
    color: var(--mark-grey);
    font-size: 78px;
  }
  .back-note {
    position: absolute;
    left: 28px;
    bottom: 22px;
    color: var(--note-light);
    font-weight: 400;
    font-size: 13px;
    letter-spacing: 0;
  }

  /* Front */
  .card--front {
    background: var(--card-light);
  }
  .card--front .wordmark {
    position: absolute;
    left: 30px;
    bottom: 50px;
    color: var(--mark-faint);
    font-size: 52px;
  }
  .contact-block {
    position: absolute;
    left: 290px;
    top: 50px;
  }
  .person-name {
    color: var(--ink);
    font-weight: 800;
    font-size: 20px;
    letter-spacing: -0.5px;
    text-transform: uppercase;
    white-space: nowrap;
  }
  .role-badge {
    display: inline-block;
    margin-top: 4px;
    padding: 2px 7px;
    background: var(--accent);
    color: var(--white);
    font-weight: 600;
    font-size: 15px;
    text-transform: uppercase;
  }
  .contact-list {
    list-style: none;
    margin-top: 18px;
  }
  .contact-item {
    display: flex;
    align-items: center;
    gap: 8px;
    color: var(--ink-soft);
    font-size: 12px;
    line-height: 22px;
    white-space: nowrap;
  }
  .contact-icon {
    width: 14px;
    height: 14px;
    flex: none;
    stroke: var(--accent);
    fill: none;
    stroke-width: 1.6;
  }
</style>
</head>
<body>

  <section class="card card--back" aria-label="Card back">
    <div class="wordmark">Pebble</div>
    <p class="back-note">Find creative pros</p>
  </section>

  <section class="card card--front" aria-label="Card front">
    <div class="wordmark">Pebble</div>
    <div class="contact-block">
      <h1 class="person-name">Gideon Thorpe</h1>
      <span class="role-badge">Owner</span>
      <ul class="contact-list">
        <li class="contact-item">
          <svg class="contact-icon" viewBox="0 0 16 16" aria-hidden="true">
            <path d="M3 2.5l2.5-.5 1.5 3-1.5 1.2a8 8 0 0 0 4.3 4.3L11 9l3 1.5-.5 2.5c-6 .8-11.3-4.5-10.5-10.5z"/>
          </svg>
          555-301-8826
        </li>
        <li class="contact-item">
          <svg class="contact-icon" viewBox="0 0 16 16" aria-hidden="true">
            <rect x="1.5" y="3.5" width="13" height="9"/>
            <path d="M1.5 3.5L8 9l6.5-5.5"/>
          </svg>
          Gideon_thorpe@quillnet.net
        </li>
        <li class="contact-item">
          <svg class="contact-icon" viewBox="0 0 16 16" aria-hidden="true">
            <circle cx="8" cy="8" r="6.5"/>
            <ellipse cx="8" cy="8" rx="2.8" ry="6.5"/>
            <path d="M1.5 8h13"/>
          </svg>
          www.workwithpebble.com
        </li>
      </ul>
    </div>
  </section>

</body>
</html>
```